Postcard Mailing 1

Our website is qrtechaid.net
We travel on site to help people/businesses with their computer issues.
This postcard is going to existing customers... just trying to touch them again.
QRT Technic provides a full line of residential and commercial computer support.

I've attached some stuff that I have done.

```html
<!DOCTYPE html>
<html lang="en">
<head>
<meta charset="utf-8">
<title>QRT Technic – Postcard Mailing</title>
<link rel="stylesheet" href="https://fonts.googleapis.com/css2?family=Lato:wght@400;700;900&family=Titillium+Web:wght@700&family=Roboto+Condensed:wght@700&display=swap">
<style>
  :root{
    --stage:#3b3b3b;
    --yellow:#f3e12b;
    --yellow-deep:#e9cf12;
    --blue:#2c45a6;
    --blue-dark:#22378a;
    --ink:#333333;
    --white:#ffffff;
    --slot:#d9d9d9;
    --photo-a:#c9c5bd;
    --photo-b:#8c8780;
    --server:#1c1c1f;
  }
  *{box-sizing:border-box;margin:0;padding:0}
  html,body{width:888px;height:1200px;overflow:hidden}
  body{background:var(--stage);font-family:'Lato',sans-serif;position:relative}
  .card{position:absolute;left:82px;width:724px;height:480px;overflow:hidden}
  .card--front{top:58px;background:radial-gradient(circle at 60% 40%,var(--yellow) 0%,var(--yellow-deep) 100%)}
  .card--back{top:648px;height:466px;background:var(--white)}
  .side-label{position:absolute;left:0;width:888px;text-align:center;color:var(--white);font:400 40px 'Lato',sans-serif;letter-spacing:1px}
  .side-label--front{top:556px}
  .side-label--back{top:1126px}
  .abs{position:absolute}
  .brand{position:absolute;color:var(--blue);font-family:'Lato',sans-serif;font-weight:900;white-space:nowrap}
  .front-brand{left:22px;top:40px;font-size:44px}
  .headline{left:18px;top:124px;font:700 45px 'Titillium Web',sans-serif;color:var(--ink);letter-spacing:-.5px;white-space:nowrap}
  .photo-frame{border-radius:0 240px 0 0;border:8px solid var(--blue);border-left:0;border-bottom:0;
    background:linear-gradient(135deg,var(--photo-a),var(--photo-b))}
  .front-photo{left:0;top:182px;width:372px;height:298px}
  .server-art{background:linear-gradient(90deg,#0e0e10,#3a3b40 45%,var(--server));border-radius:4px}
  .front-servers{left:562px;top:26px;width:150px;height:150px}
  .services{left:453px;top:172px;width:271px;height:118px;background:var(--blue);border-radius:6px 0 0 6px;padding:8px 0 0 14px;list-style:none}
  .services li{color:var(--white);font-size:17px;line-height:25.5px}
  .services li::before{content:"➤";font-size:11px;margin-right:10px;vertical-align:2px}
  .housecalls{right:18px;top:304px;text-align:right;font:700 39px/44px 'Roboto Condensed',sans-serif;color:var(--ink)}
  .phone-bar{left:338px;top:400px;width:386px;height:50px;background:var(--blue);border-radius:6px 0 0 6px;color:var(--white);
    font:400 41px/50px 'Lato',sans-serif;padding-left:36px}
  .phone-bar svg{position:absolute;left:10px;top:14px}
  .burst{position:absolute}
  .burst text{font-family:'Lato',sans-serif;font-weight:700;text-anchor:middle}
  /* back */
  .back-panel{left:0;top:0;width:387px;height:466px;background:radial-gradient(circle at 60% 40%,var(--yellow),var(--yellow-deep))}
  .back-photo{left:0;top:0;width:266px;height:182px}
  .back-servers{left:232px;top:16px;width:142px;height:142px}
  .care-box{left:28px;top:142px;width:133px;height:130px;background:var(--blue);padding:8px 8px 0 8px;color:var(--white);border-radius:3px}
  .care-box h3{font:700 15px/18px 'Lato',sans-serif;color:var(--yellow);margin-bottom:3px}
  .care-box ul{list-style:none}
  .care-box li{font-size:12px;line-height:17.6px}
  .care-box li::before{content:"➤";font-size:8px;margin-right:4px;vertical-align:1px;color:var(--yellow)}
  .portrait{left:223px;top:198px;width:130px;height:130px;border-radius:50%;border:3px solid var(--white);
    background:radial-gradient(circle,#e8d3b5,#b89c74)}
  .plan{left:14px;top:280px;font-size:19px;color:var(--ink)}
  .plan strong{color:var(--blue)}
  .plan-url{left:14px;top:306px;font-size:18px;font-weight:700;color:var(--ink)}
  .back-band{left:0;top:332px;width:387px;height:134px;background:var(--blue)}
  .offer{left:15px;top:343px;width:365px;height:36px;background:var(--yellow);border-radius:18px;
    font:900 italic 22px/36px 'Lato',sans-serif;color:var(--ink);text-align:center}
  .contact{left:28px;color:var(--white);font-size:23px;display:flex;align-items:center;gap:8px}
  .contact--phone{top:385px}
  .contact--web{top:414px}
  .stamp-slot{left:577px;top:17px;width:133px;height:135px;background:var(--slot)}
  .address-slot{left:426px;top:164px;width:281px;height:181px;background:var(--slot)}
  .back-brand{right:16px;top:412px;font-size:26px}
</style>
</head>
<body>

<section class="card card--front">
  <div class="brand front-brand">QRT Technic</div>
  <h1 class="abs headline">LET US COME TO YOU!</h1>

  <div class="abs photo-frame front-photo" role="img" aria-label="Photo of a technician connecting cables to a desktop computer while an older customer watches"></div>

  <div class="abs server-art front-servers" role="img" aria-label="Illustration of three black server towers"></div>

  <svg class="burst" style="left:420px;top:34px" width="116" height="116" viewBox="0 0 120 120">
    <polygon fill="var(--blue)" points="60,0 67,14 80,4 82,20 97,15 93,30 110,30 101,44 117,50 104,60 117,70 101,76 110,90 93,90 97,105 82,100 80,116 67,106 60,120 53,106 40,116 38,100 23,105 27,90 10,90 19,76 3,70 16,60 3,50 19,44 10,30 27,30 23,15 38,20 40,4 53,14"/>
    <text x="60" y="45" fill="#fff" font-size="12">"If We Can't</text>
    <text x="60" y="60" fill="#fff" font-size="12">Fix It...</text>
    <text x="60" y="76" fill="var(--yellow)" font-size="13">YOU DON'T</text>
    <text x="60" y="92" fill="var(--yellow)" font-size="13">PAY!"</text>
  </svg>

  <svg class="burst" style="left:310px;top:180px" width="130" height="130" viewBox="0 0 120 120">
    <polygon fill="var(--blue)" points="60,0 67,14 80,4 82,20 97,15 93,30 110,30 101,44 117,50 104,60 117,70 101,76 110,90 93,90 97,105 82,100 80,116 67,106 60,120 53,106 40,116 38,100 23,105 27,90 10,90 19,76 3,70 16,60 3,50 19,44 10,30 27,30 23,15 38,20 40,4 53,14"/>
    <text x="60" y="40" fill="#fff" font-size="12">Most</text>
    <text x="60" y="55" fill="#fff" font-size="11.5">Appointments</text>
    <text x="60" y="72" fill="var(--yellow)" font-size="13">WITHIN 24</text>
    <text x="60" y="88" fill="var(--yellow)" font-size="13">HOURS!</text>
  </svg>

  <ul class="abs services">
    <li>Virus / Spyware Cleanup</li>
    <li>Computer Setup</li>
    <li>Wireless Networks</li>
    <li>Data Transfer / Recovery</li>
  </ul>

  <p class="abs housecalls">We Make<br>Housecalls!</p>

  <div class="abs phone-bar">
    <svg width="20" height="24" viewBox="0 0 20 24"><path fill="var(--yellow)" d="M4 1l4 6-3 3c1 4 4 7 7 9l3-3 5 4-3 4C8 23-2 11 1 3z"/></svg>
    555-318-2760
  </div>
</section>
<div class="side-label side-label--front">FRONT</div>

<section class="card card--back">
  <div class="abs back-panel"></div>
  <div class="abs photo-frame back-photo" role="img" aria-label="Photo of a woman sitting under a desk tangled in computer cables"></div>
  <div class="abs server-art back-servers" role="img" aria-label="Illustration of three black server towers"></div>

  <div class="abs care-box">
    <h3>QRT TAKES<br>CARE OF</h3>
    <ul>
      <li>Virus Protection</li>
      <li>Data Backups</li>
      <li>System Updates</li>
      <li>Unlimited Support</li>
    </ul>
  </div>

  <div class="abs portrait" role="img" aria-label="Round portrait photo of a smiling customer"></div>

  <p class="abs plan">Just <strong>$19.95</strong> a month!</p>
  <p class="abs plan-url">www.techcareplan.com</p>

  <div class="abs back-band"></div>
  <div class="abs offer">MENTION THIS AD FOR 20%</div>
  <p class="abs contact contact--phone">
    <svg width="14" height="17" viewBox="0 0 20 24"><path fill="var(--yellow)" d="M4 1l4 6-3 3c1 4 4 7 7 9l3-3 5 4-3 4C8 23-2 11 1 3z"/></svg>
    (555) 318-2760
  </p>
  <p class="abs contact contact--web">
    <svg width="14" height="14" viewBox="0 0 14 14"><circle cx="7" cy="7" r="6" fill="none" stroke="var(--yellow)" stroke-width="1.6"/><path d="M1 7h12M7 1c-3 3-3 9 0 12M7 1c3 3 3 9 0 12" fill="none" stroke="var(--yellow)" stroke-width="1.2"/></svg>
    www.qrtechaid.net
  </p>

  <div class="abs stamp-slot"></div>
  <div class="abs address-slot"></div>
  <div class="brand back-brand">QRT Technic</div>
</section>
<div class="side-label side-label--back">BACK</div>

</body>
</html>
```